Starting meadery needs logo and label design

We are starting to show our hand crafted meads to potential investors and need a professional logo and label to properly show how serious this proj...

Target Market(s)

Craft beer drinker searching for a new experience. People who are beer drinkers aspiring to be wine drinker.

Industry/Entity Type

It Professional

Requirements
Must have
• Professional design. Not overly ornate. Simple use of colors for low cost startup printing.

```html
<!DOCTYPE html>
<html lang="en">
<head>
<meta charset="utf-8">
<title>Ninefold Meadery – Spiced Orange Mead Label</title>
<link rel="stylesheet" href="https://fonts.googleapis.com/css2?family=Righteous&family=Bungee&family=Satisfy&family=Dancing+Script:wght@500&display=block">
<style>
  :root {
    --paper: #f0eef1;
    --ink: #1f1b12;
    --honey: #8c5518;
    --badge-fill: #ffffff;
  }
  * { margin: 0; padding: 0; box-sizing: border-box; }
  html, body { width: 901px; height: 1200px; overflow: hidden; background: var(--paper); }
  .label {
    position: relative;
    width: 901px;
    height: 1200px;
    background: var(--paper);
    color: var(--ink);
  }
  .brand-mark {
    position: absolute;
    left: 0;
    top: 0;
    width: 901px;
    height: 720px;
  }
  .brand-name {
    position: absolute;
    left: 0;
    top: 258px;
    width: 901px;
    text-align: center;
    font-family: "Righteous", sans-serif;
    font-weight: 400;
    font-size: 92px;
    line-height: 1.12;
    letter-spacing: 4px;
    text-transform: uppercase;
    color: var(--honey);
  }
  .flavour {
    position: absolute;
    left: 0;
    top: 724px;
    width: 901px;
    text-align: center;
    font-family: "Righteous", sans-serif;
    font-size: 52px;
    line-height: 1.2;
    color: var(--ink);
  }
  .product {
    position: absolute;
    left: 8px;
    top: 796px;
    width: 901px;
    text-align: center;
    font-family: "Bungee", sans-serif;
    font-weight: 400;
    font-size: 124px;
    line-height: 1;
    letter-spacing: 18px;
    color: var(--ink);
    text-shadow: -5px 5px 0 var(--paper), -8px 8px 0 var(--ink);
  }
  .description {
    position: absolute;
    left: 30px;
    top: 978px;
    width: 841px;
    text-align: center;
    font-family: "Satisfy", "Dancing Script", cursive;
    font-size: 29px;
    line-height: 50px;
    white-space: nowrap;
    color: var(--ink);
  }
</style>
</head>
<body>
  <main class="label">
    <svg class="brand-mark" viewBox="0 0 901 720" aria-hidden="true">
      <circle cx="450" cy="360" r="318" fill="var(--badge-fill)" stroke="var(--ink)" stroke-width="24"/>
    </svg>
    <h1 class="brand-name">Ninefold<br>Meadery</h1>

    <p class="flavour">Spiced orange</p>
    <h2 class="product">MEAD</h2>

    <p class="description">
      Lorem ipsum dolor sit amet, Lorem ipsum dolor sit amet,<br>
      consectetuer adipiscing elit, sed diam nonummy nibh<br>
      euismod tincidunt ut laoreet dolore magna aliquam erat<br>
      volutpat. Ut wisi enim ad minim veniam, quis nostrud
    </p>
  </main>
</body>
</html>
```